Geschäftspapiere für familiengeführtes Zeitarbeitsunternehmen
Zielgruppe
Wir sind ein familiengeführtes Zeitarbeitsunternehmen. Somit haben wir 2 Zielgruppen, unsere Kunden und unsere Mitarbeiter. Eine Übersicht von uns findet man am besten auf unserer Website www.brandt-kraefte.de
Aufgabenstellung
Wir möchten 'nur' angepasstes Briefpapier mit neuen Daten. Gerne können Sie uns auch Vorschläge bezüglich eines verbesserten Designs machen.
Folgende Änderungen sind zu verarbeiten:
- die Geschäftstellen in Neustadt und Zell wurde geschlossen, daher ist Oberhof nun Hauptgeschäftsstelle
- die Firmierung hat sich geändert: das pw wurde entfernt
- Plaudernetz und bildoria kann raus
- Neu: UID DE 31 47 26 804
- Neu: Amtgericht Jena HRB 742391
- Neu rein bitte noch: Hinweis zum Datenschutz: https://brandt-kraefte.de/datenschutz/

```html
<!DOCTYPE html>
<html lang="de">
<head>
<meta charset="utf-8">
<title>Briefpapier – Brandt Personal GmbH</title>
<link href="https://fonts.googleapis.com/css2?family=Roboto:wght@300;400;500&display=swap" rel="stylesheet">
<style>
  :root {
    --brand-blue: #0181ac;
    --text-grey: #6e6e6e;
    --footer-grey: #6f6f6e;
    --paper: #ffffff;
  }
  * { margin: 0; padding: 0; box-sizing: border-box; }
  html, body {
    width: 848px; height: 1200px; overflow: hidden;
    background: var(--paper);
  }
  .letterhead {
    position: relative;
    width: 848px; height: 1200px;
    font-family: "Roboto", sans-serif;
    font-weight: 300;
    color: var(--text-grey);
    overflow: hidden;
  }
  .header-band {
    position: absolute; left: 0; top: 0;
    width: 100%; height: 81px;
    background: var(--brand-blue);
    z-index: 2;
  }
  .header-shadow {
    position: absolute; left: 8px; right: 8px; top: 81px;
    height: 40px;
    background: linear-gradient(to bottom, rgba(40,40,40,.75) 0%, rgba(90,90,90,.35) 35%, rgba(255,255,255,0) 100%);
    border-radius: 0 0 50% 50% / 0 0 20% 20%;
    filter: blur(2px);
    z-index: 1;
  }
  .brand-mark {
    position: absolute; right: 137px; top: 96px;
    display: flex; align-items: center; gap: 8px;
    z-index: 3;
  }
  .brand-mark__dot {
    width: 14px; height: 14px; border-radius: 50%;
    background: var(--brand-blue);
  }
  .brand-mark__name {
    font-weight: 500;
    font-size: 30px;
    letter-spacing: 1px;
    color: var(--brand-blue);
    line-height: 1;
  }
  .sender-line {
    position: absolute; left: 80px; top: 206px;
    font-size: 10.8px;
    letter-spacing: 0.05px;
  }
  .company-info {
    position: absolute; left: 575px; top: 205px;
    font-size: 13px;
    line-height: 15.5px;
  }
  .company-info p + p { margin-top: 15.5px; }
  .footer-band {
    position: absolute; left: 0; bottom: 0;
    width: 100%; height: 33px;
    background: var(--footer-grey);
    display: flex; align-items: center;
    padding-left: 80px;
  }
  .privacy-note {
    color: #ffffff;
    font-size: 13px;
    font-weight: 300;
  }
</style>
</head>
<body>
  <div class="letterhead">
    <div class="header-band"></div>
    <div class="header-shadow"></div>

    <div class="brand-mark">
      <span class="brand-mark__dot"></span>
      <span class="brand-mark__name">Brandt Personal</span>
    </div>

    <div class="sender-line">Brandt Personal GmbH · Lindenhainer Straße 7 · D-98562 Talheim</div>

    <div class="company-info">
      <p>Brandt Personal GmbH<br>Lindenhainer Straße 7<br>D-98562 Talheim</p>
      <p>Tel: +49 36811 472 310<br>Fax: +49 36811 472 315<br>E-Mail: kontakt@brandt-kraefte.de<br>www.brandt-kraefte.de</p>
      <p>Geschäftsführer: Marlo Brandt<br>UID: DE 31 47 26 804</p>
      <p>Amtsgericht Jena<br>HRB 742391</p>
    </div>

    <div class="footer-band">
      <span class="privacy-note">Hinweis zum Datenschutz: https://brandt-kraefte.de/datenschutz/</span>
    </div>
  </div>
</body>
</html>
```